Defense contractor needs a roll-up for an exhibition

The booth we have booked has only a size of 3m².
So this will be the centerpiece of the whole booth.
We need a roll-up that attracts visitors and at the same time it should contain already designed graphics. These graphics are giving visitors an overview of our system. So it is necessary to have them exposed in a height that the booth personal can conveniently point with its fingers at them.
For information about our company and product visit:
https://www.brightlanternoptics.com/
For designing you should use Adobe Illustrator and the templates provided in the zip file, to guarantee a perfect print.
I have supplied my business card that you can copy the logo. As the company logo will be already at the booth nearby the top of the roll-up, you should not place it there. It can be in the middle or at the bottom.
I have uploaded a picture of the booth. The roll up will be placed at the left of the screen and has a size of 80cm x 200cm

Defense

Defense

Serif

Colors
0054AA
0677BA
7BADD7
CADEEF
E8F1F8

• you must use the Adobe Illustrator template to have a good printing result
• company logo on the upper side of the roll-up

```html
<!DOCTYPE html>
<html lang="en">
<head>
<meta charset="utf-8">
<title>TRACIS Roll-up</title>
<link href="https://fonts.googleapis.com/css2?family=Ubuntu:wght@500;700&family=Source+Sans+3:wght@400;600&display=swap" rel="stylesheet">
<style>
  :root {
    --ink: #111111;
    --paper-light: #f2f2f2;
    --paper-mid: #d9d9d9;
    --paper-dark: #b8b8b8;
    --panel: #f7f7f7;
    --banner: #a3a3a3;
    --rule: #6d6d6d;
    --art-light: #e9e9e9;
    --art-dark: #a9a9a9;
  }
  * { margin: 0; padding: 0; box-sizing: border-box; }
  html, body { width: 1200px; height: 2824px; overflow: hidden; }
  body {
    position: relative;
    color: var(--ink);
    font-family: "Source Sans 3", "Myriad Pro", sans-serif;
    background: radial-gradient(ellipse at 70% 35%, var(--paper-light) 0%, var(--paper-mid) 55%, var(--paper-dark) 100%);
  }
  .headline {
    position: absolute; left: 60px; top: 72px;
    font-family: "Ubuntu", sans-serif; font-weight: 700;
    font-size: 57px; line-height: 72px;
  }
  .intro {
    position: absolute; left: 60px; top: 272px; width: 1130px;
    font-size: 41px; line-height: 52px; letter-spacing: -0.3px;
  }
  .intro .product-name {
    font-family: "Ubuntu", sans-serif; font-weight: 700; font-size: 35px; line-height: 52px;
  }
  .art {
    position: absolute;
    background: radial-gradient(ellipse at center, var(--art-light) 0%, var(--art-dark) 100%);
    border-radius: 12px; opacity: 0.85;
  }
  .art-range { left: 640px; top: 288px; width: 530px; height: 510px; }
  .art-debrief { left: 60px; top: 1692px; width: 640px; height: 520px; }
  .features-panel {
    position: absolute; left: 38px; top: 1032px; width: 1124px; height: 576px;
    background: var(--panel);
  }
  .features-banner {
    position: absolute; left: 284px; top: 964px; width: 610px; height: 90px;
    background: var(--banner); opacity: 0.9;
    font-family: "Ubuntu", sans-serif; font-weight: 700; font-size: 54px;
    display: flex; align-items: center; justify-content: center;
  }
  .feature {
    position: absolute; top: 1086px; width: 360px;
    text-align: center; font-size: 42px; line-height: 54px;
  }
  .feature svg { display: block; margin: 0 auto 14px; height: 104px; }
  .feature-deploy { left: 48px; }
  .feature-vehicles { left: 420px; }
  .feature-sensors { left: 804px; }
  .divider { position: absolute; top: 1086px; width: 2px; height: 474px; background: var(--rule); }
  .divider-a { left: 403px; }
  .divider-b { left: 788px; }
  .debrief-title {
    position: absolute; right: 74px; top: 1664px; text-align: right;
    font-family: "Ubuntu", sans-serif; font-weight: 700; font-size: 56px; line-height: 72px;
  }
  .debrief-copy {
    position: absolute; left: 70px; top: 2240px; width: 1070px;
    font-size: 38px; line-height: 52px; text-align: justify; hyphens: auto;
  }
  .brand-name {
    position: absolute; left: 72px; top: 2626px; width: 1076px;
    font-family: "Ubuntu", sans-serif; font-weight: 700; font-size: 78px;
    letter-spacing: 1px; text-transform: uppercase; white-space: nowrap;
  }
</style>
</head>
<body>
  <h1 class="headline">Advanced Combat Training Systems<br>for Realistic Combat Simulation</h1>

  <div class="art art-range" role="img" aria-label="Illustration of tanks, range targets and a mobile instructor truck with monitors and soldiers"></div>

  <p class="intro"><span class="product-name">TRACIS (Tactical Range<br>Acquisition and Combat<br>Instrumentation System)</span><br>allows for a modern<br>approach to duel<br>simulation, firing range<br>training, armored<br>vehicle driving training,<br>and simulation debriefing<br>through an integrated system of<br>sensors, optics, and controls that<br>give soldiers and instructors real-time, real-world vision and data.</p>

  <section class="features-panel"></section>
  <h2 class="features-banner">Features of TRACIS</h2>

  <div class="feature feature-deploy">
    <svg viewBox="0 0 100 104" aria-hidden="true">
      <rect x="40" y="2" width="20" height="8" fill="#111"/>
      <line x1="80" y1="16" x2="88" y2="8" stroke="#111" stroke-width="7"/>
      <circle cx="50" cy="58" r="38" fill="none" stroke="#111" stroke-width="10"/>
      <polyline points="50,34 50,60 64,70" fill="none" stroke="#111" stroke-width="8" stroke-linecap="round"/>
    </svg>
    Full deployment<br>of unique<br>equipment<br>takes no more<br>than 20<br>minutes
  </div>
  <div class="feature feature-vehicles">
    <svg viewBox="0 0 270 100" aria-hidden="true">
      <rect x="0" y="22" width="110" height="8" fill="#111"/>
      <path d="M100 12 H200 L215 40 H85 Z" fill="#111"/>
      <path d="M70 46 H240 L265 58 L240 96 H60 L50 58 Z" fill="#111"/>
      <g fill="#fff"><circle cx="92" cy="76" r="10"/><circle cx="122" cy="76" r="10"/><circle cx="152" cy="76" r="10"/><circle cx="182" cy="76" r="10"/><circle cx="212" cy="76" r="10"/></g>
    </svg>
    Designed to<br>equip armored<br>vehicles and<br>weapons systems,<br>regardless of the<br>type of<br>manufacturer
  </div>
  <div class="feature feature-sensors">
    <svg viewBox="0 0 140 100" aria-hidden="true">
      <g fill="#111">
        <rect x="22" y="2" width="7" height="14"/><rect x="40" y="2" width="7" height="14"/><rect x="58" y="2" width="7" height="14"/><rect x="76" y="2" width="7" height="14"/><rect x="94" y="2" width="7" height="14"/><rect x="112" y="2" width="7" height="14"/>
        <rect x="22" y="84" width="7" height="14"/><rect x="40" y="84" width="7" height="14"/><rect x="58" y="84" width="7" height="14"/><rect x="76" y="84" width="7" height="14"/><rect x="94" y="84" width="7" height="14"/><rect x="112" y="84" width="7" height="14"/>
        <rect x="52" y="32" width="36" height="36" rx="4"/>
      </g>
      <rect x="8" y="18" width="124" height="64" rx="10" fill="none" stroke="#111" stroke-width="8"/>
    </svg>
    Has a set of<br>advanced sensors<br>and tools for the<br>most realistic and<br>productive<br>combat<br>simulation
  </div>
  <div class="divider divider-a"></div>
  <div class="divider divider-b"></div>

  <div class="art art-debrief" role="img" aria-label="Illustration of a debriefing room with instructors at desks facing two wall screens"></div>
  <h2 class="debrief-title">Debriefing with<br>TRACIS</h2>

  <p class="debrief-copy">TRACIS equips instructors with comprehensive data collection of training elements allowing for an immersive, insightful, and detailed debriefing process. All data contents can be easily recorded, edited, and archived for reference. TRACIS features mobile container functionality for rapid deployment or a compact stationary workplace.</p>

  <div class="brand-name">Bright Lantern Optics</div>
</body>
</html>
```